Hadley & Partners, LLC Business Card 2016

We need a new business card design for a very important trade show coming up.

We are a compliance Consulting Firm. Our clients are stock brokerage firms and investment advisers.

I would like our logo on both sides of the card.

Info in the front of the card shold include:

Logo
First & Last Name
Title
Office #
Cell #
Email
Company Address (42 W. Calloway St., Suite 300 Pasadena, CA 91417

Back of the card should include the logo and url: www.hadleypartnersgroup.com

Target Market(s)

Stock Brokerage Firms and Investment Advisers

Industry/Entity Type

Financial Service

Contact Information for Business Card

Marcus J. Pellew
President
42 W. Calloway St., Suite 300
Pasadena, CA 91417
O 626.555.0147 ext. 204
C 818.555.0193
Email: marcus@hadleypartnersgroup.com
www.hadleypartnersgroup.com

Requirements
Nice to have
• The back of the card could be black with the logo with the white letters.
• I do want the front of the card to at least have the color logo with the black "Hadley & Partners Lettering.

```html
<!DOCTYPE html>
<html lang="en">
<head>
<meta charset="utf-8">
<title>Hadley &amp; Partners — Business Card</title>
<link rel="stylesheet" href="https://fonts.googleapis.com/css2?family=PT+Sans:wght@400;700&family=PT+Sans+Narrow:wght@700&display=swap">
<style>
  :root {
    --page-bg: #c9cacd;
    --card-white: #ffffff;
    --card-black: #050505;
    --ink: #231f20;
    --ink-soft: #2e2e2e;
    --brand-red: #8e1a17;
    --accent-red: #d0342c;
    --rule-grey: #bfbfbf;
    --band-grey-light: #a9abaf;
    --band-grey-dark: #3f4148;
  }
  * { box-sizing: border-box; margin: 0; padding: 0; }
  html, body { width: 1200px; height: 1200px; overflow: hidden; }
  body {
    background: var(--page-bg);
    font-family: "PT Sans", Arial, sans-serif;
    position: relative;
  }
  .card {
    position: absolute;
    left: 239px;
    width: 722px;
    height: 413px;
    overflow: hidden;
  }
  .card--back { top: 162px; background: var(--card-black); }
  .card--front { top: 612px; background: var(--card-white); }

  .back-texture {
    position: absolute; inset: 0;
    background: radial-gradient(ellipse at 40% 40%, #141414 0%, #070707 60%, #030303 100%);
  }

  .brand {
    position: absolute;
    display: flex;
    align-items: center;
    gap: 14px;
    font-family: "PT Sans", Arial, sans-serif;
    font-weight: 700;
    letter-spacing: 1px;
    white-space: nowrap;
  }
  .brand__square {
    width: 46px; height: 46px;
    background: var(--accent-red);
    flex: none;
  }
  .brand__name { font-size: 33px; line-height: 1; }
  .card--back .brand { right: 26px; bottom: 22px; color: #ffffff; }
  .card--front .brand { left: 26px; top: 64px; color: var(--ink); }

  .person {
    position: absolute;
    right: 25px;
    top: 161px;
    text-align: right;
  }
  .person__name {
    font-family: "PT Sans Narrow", "Arial Narrow", sans-serif;
    font-weight: 700;
    font-size: 24px;
    color: var(--brand-red);
    line-height: 1;
    letter-spacing: 0.3px;
  }
  .person__title {
    font-size: 17.5px;
    color: var(--ink-soft);
    margin-top: 8px;
  }
  .divider {
    position: absolute;
    left: 26px; right: 25px; top: 226px;
    height: 2px;
    background: var(--rule-grey);
  }

  .contact-list {
    position: absolute;
    left: 26px; top: 277px;
    list-style: none;
  }
  .contact-list li {
    display: flex; align-items: center;
    height: 32.5px;
    font-size: 17.5px;
    color: var(--ink-soft);
  }
  .contact-icon { width: 22px; height: 22px; margin-right: 10px; flex: none; }

  .address {
    position: absolute;
    right: 25px; top: 285px;
    text-align: right;
    font-style: normal;
    font-size: 17.5px;
    color: var(--ink-soft);
    line-height: 24px;
  }
  .address__web {
    display: block;
    margin-top: 8px;
    font-weight: 700;
    color: var(--brand-red);
  }
  .footer-band {
    position: absolute;
    left: 0; bottom: 0;
    width: 722px; height: 26px;
  }
</style>
</head>
<body>

  <section class="card card--back" aria-label="Card back">
    <div class="back-texture" role="img" aria-label="Faint repeating brand pattern on black"></div>
    <div class="brand">
      <span class="brand__square"></span>
      <span class="brand__name">HADLEY &amp; PARTNERS</span>
    </div>
  </section>

  <section class="card card--front" aria-label="Card front">
    <div class="brand">
      <span class="brand__square"></span>
      <span class="brand__name">HADLEY &amp; PARTNERS</span>
    </div>

    <div class="person">
      <p class="person__name">MARCUS J. PELLEW</p>
      <p class="person__title">President</p>
    </div>

    <div class="divider"></div>

    <ul class="contact-list">
      <li>
        <svg class="contact-icon" viewBox="0 0 22 22" aria-hidden="true">
          <circle cx="11" cy="11" r="11" fill="var(--brand-red)"/>
          <path d="M7.2 5.6l2 2.1-1 1.4c.7 1.6 2 2.9 3.6 3.7l1.4-1 2.1 2-1.2 1.8c-3.8-.6-7.2-4-7.8-7.8z" fill="#fff"/>
        </svg>
        626.555.0147 ext. 204
      </li>
      <li>
        <svg class="contact-icon" viewBox="0 0 22 22" aria-hidden="true">
          <circle cx="11" cy="11" r="11" fill="var(--brand-red)"/>
          <rect x="7.5" y="4.8" width="7" height="12.4" rx="1.2" fill="#fff"/>
          <rect x="8.6" y="6.3" width="4.8" height="8" fill="var(--brand-red)"/>
        </svg>
        818.555.0193
      </li>
      <li>
        <svg class="contact-icon" viewBox="0 0 22 22" aria-hidden="true">
          <circle cx="11" cy="11" r="11" fill="var(--brand-red)"/>
          <rect x="5.5" y="7" width="11" height="8" fill="#fff"/>
          <path d="M5.5 7l5.5 4.5L16.5 7" fill="none" stroke="var(--brand-red)" stroke-width="1.2"/>
        </svg>
        marcus@hadleypartnersgroup.com
      </li>
    </ul>

    <address class="address">
      42 W. Calloway St., Suite 300<br>
      Pasadena, CA 91417
      <span class="address__web">www.hadleypartnersgroup.com</span>
    </address>

    <svg class="footer-band" viewBox="0 0 722 26" preserveAspectRatio="none" aria-hidden="true">
      <defs>
        <linearGradient id="bandGrey" x1="0" x2="1" y1="0" y2="0">
          <stop offset="0" stop-color="var(--band-grey-light)"/>
          <stop offset="1" stop-color="var(--band-grey-dark)"/>
        </linearGradient>
        <linearGradient id="bandRed" x1="0" x2="1" y1="0" y2="0">
          <stop offset="0" stop-color="#e0423a"/>
          <stop offset="1" stop-color="#b8241f"/>
        </linearGradient>
      </defs>
      <polygon points="0,0 433,0 425,26 0,26" fill="url(#bandGrey)"/>
      <polygon points="441,0 722,0 722,26 433,26" fill="url(#bandRed)"/>
    </svg>
  </section>

</body>
</html>
```